Web Design Project

We are a business based in Sydney Australia, we have a very cool and sophisticated AI platform that lets you create Virtual Agents mainly for Enterprise clients but we are now moving into the Personal AI space where we will have mobile apps using our technology. We need a new look and feel with some better branding

We will progress this in stages with a quick touch up to our site followed by a more thorough rebuild.

So for now, on our web site, stage 1.... I'm happy to change colours, we will keep the "head" in our logo but change our name. if you look at out site at www.myvelornexa.com you will see that there is content but not much structure...we will include videos at some point and some infographics but not just yet ....so I'm after a suite of 3 different template designs that we can use and I want to work with the successful designer to tweak them and populate them with a lot of our current content.

We will keep our avatar but she may need a makeover...I'm open to suggestions on how to make our site more progressive. Would a more tiled, pavilio 6 look and feel work?

I would prefer to use word press

Target Market(s)

mainly enterprise clients, big banks, insurance companies, telcos

Industry/Entity Type

Business

Requirements
Nice to have
• check out some of our competitors....brindLO, QuallaTep, marvel drift, foravento, quorabellink, oPrax

I was thinking that a more tiled 'pavilio 6' look and feel might be good...open to suggestions
Should not have
• can't look cheap and nasty

```html
<!DOCTYPE html>
<html lang="en">
<head>
<meta charset="utf-8">
<title>myVelorNexa – Virtual Assistants</title>
<link rel="stylesheet" href="https://fonts.googleapis.com/css2?family=Source+Sans+3:wght@400;600;700&display=swap">
<style>
  :root {
    --green: #2f6b5c;
    --green-drop: #3a7464;
    --green-light: #93bdb1;
    --orange: #ef7d12;
    --heading-orange: #e46e19;
    --panel: #dcdcdc;
    --card: #f8f8f8;
    --text: #333;
    --muted: #777;
    --nav-text: #cfe2dc;
  }
  * { box-sizing: border-box; margin: 0; padding: 0; }
  html, body { width: 1200px; height: 1200px; overflow: hidden; background: #fff; }
  body { position: relative; font-family: "Source Sans 3", sans-serif; color: var(--text); }
  .abs { position: absolute; }

  .brand { left: 145px; top: 124px; font-size: 26px; font-weight: 600; letter-spacing: 1px; color: #222; display: flex; align-items: center; gap: 8px; }
  .brand .dot { width: 22px; height: 22px; background: var(--green); border-radius: 50%; }

  .login-label { left: 662px; top: 137px; font-size: 12px; color: #444; }
  .field { top: 135px; height: 20px; width: 113px; border-radius: 10px; background: #e3e3e3; font-size: 12px; color: #555; padding: 2px 9px; }
  .forgot { top: 158px; font-size: 10px; color: #888; }
  .login-btn { left: 1009px; top: 135px; width: 61px; height: 20px; background: var(--orange); color: #fff; font-size: 12px; text-align: center; line-height: 20px; }

  .nav { left: 130px; top: 196px; width: 940px; height: 43px; background: var(--green); border-radius: 8px 8px 0 0; }
  .nav-item { top: 13px; font-size: 14px; color: var(--nav-text); }
  .nav-item.active { color: #fff; font-weight: 600; }
  .search { left: 762px; top: 8px; width: 167px; height: 26px; border-radius: 7px; background: var(--green-light); font-size: 11px; color: #2d5a4e; font-weight: 600; padding: 6px 8px; }

  .dropdown { left: 305px; top: 239px; width: 211px; height: 135px; background: var(--green-drop); z-index: 5; }
  .dropdown span { position: absolute; left: 13px; font-size: 12px; color: #9cc1b6; font-weight: 600; }
  .dropdown span.active { color: #fff; }

  .video { left: 130px; top: 268px; width: 380px; height: 232px; background: var(--panel); }
  .video-screen { left: 8px; top: 9px; width: 364px; height: 196px; background: #fff; }

  .promo { left: 530px; top: 267px; width: 540px; height: 322px; background: #f2f2f2; border: 1px solid #c8c8c8; overflow: hidden; }
  .promo h1 { position: absolute; left: 27px; top: 18px; font-size: 18px; font-weight: 400; color: #333; }
  .promo .sub { position: absolute; left: 28px; top: 40px; font-size: 13px; color: #666; }
  .avatar { left: 0; top: 82px; width: 190px; height: 240px;
    background: radial-gradient(ellipse 60% 70% at 48% 55%, #79c4a6 0%, #4f9d96 35%, #3a6f82 62%, rgba(242,242,242,0) 100%); }
  .plan { font-size: 12px; color: #333; line-height: 14.5px; z-index: 2; }
  .plan h2 { font-size: 14px; font-weight: 600; color: var(--heading-orange); margin-bottom: 9px; }
  .plan li { list-style: none; }
  .plan.ticks li::before { content: "➜"; color: var(--green); font-size: 9px; margin-right: 6px; }
  .plan.highlight { background: #e3e3e3; border-radius: 6px; }
  .start { width: 61px; height: 16px; background: var(--green); color: #fff; font-size: 9px; font-weight: 700; text-align: center; line-height: 16px; border-radius: 4px; z-index: 3; }

  .team { left: 130px; top: 617px; width: 940px; height: 336px; background: var(--panel); }
  .member { top: 9px; width: 200px; height: 308px; background: var(--card); text-align: center; }
  .member h3 { margin-top: 8px; font-size: 18px; font-weight: 400; color: #222; }
  .member h3 small { font-size: 13px; color: #555; }
  .member .photo { margin: 11px auto 0; width: 118px; height: 117px; border: 1px solid #ccc;
    background: linear-gradient(160deg, #eef3f1 0%, #d9e4e0 55%, #c6d5cf 100%); }
  .member ul { margin-top: 22px; list-style: none; font-size: 12px; color: #777; line-height: 14.5px; }

  .partners { left: 130px; top: 988px; width: 940px; height: 89px; background: #f4f4f4; display: flex; justify-content: space-around; align-items: center; }
  .partner { font-size: 26px; color: #777; display: flex; align-items: center; gap: 8px; }
  .partner i { width: 14px; height: 14px; background: #999; border-radius: 50%; }
</style>
</head>
<body>
  <div class="abs brand"><span>myVELORNEXA</span><span class="dot"></span></div>

  <div class="abs login-label">Existing Customers:</div>
  <div class="abs field" style="left:769px">username</div>
  <div class="abs field" style="left:889px">password</div>
  <div class="abs login-btn">Login</div>
  <div class="abs forgot" style="left:776px">Forgot username?</div>
  <div class="abs forgot" style="left:898px">Forgot password?</div>

  <nav class="abs nav">
    <span class="abs nav-item" style="left:13px">Home</span>
    <span class="abs nav-item" style="left:77px">Technology</span>
    <span class="abs nav-item active" style="left:175px">Products</span>
    <span class="abs nav-item" style="left:257px">Our Velor Nexas</span>
    <span class="abs nav-item" style="left:382px">Latest News</span>
    <span class="abs nav-item" style="left:480px">The Company</span>
    <span class="abs nav-item" style="left:591px">FAQ</span>
    <div class="abs search">search site</div>
  </nav>

  <div class="abs dropdown">
    <span style="top:16px">Product 1</span>
    <span class="active" style="top:45px">Product 2</span>
    <span style="top:74px">Product 3</span>
    <span style="top:102px">Product 4</span>
  </div>

  <div class="abs video">
    <div class="abs video-screen"></div>
    <svg class="abs" style="left:128px;top:55px" width="122" height="122" viewBox="0 0 122 122" aria-label="Play video">
      <circle cx="61" cy="59" r="56" fill="none" stroke="#bdbdbd" stroke-width="6"/>
      <polygon points="48,38 48,80 86,59" fill="#bdbdbd"/>
    </svg>
  </div>

  <section class="abs promo">
    <h1>Start Building Your Virtual Assistant Now!</h1>
    <p class="sub">MyVelorNexas virtual agents are ready for your command</p>
    <div class="abs avatar" role="img" aria-label="Digital virtual assistant avatar in green and blue tones"></div>

    <div class="abs plan highlight ticks" style="left:169px;top:77px;width:177px;height:118px;padding:2px 11px">
      <h2>Enterprise</h2>
      <ul>
        <li>Advanced customer support</li>
        <li>Sophisticated visual avatar</li>
        <li>Advanced analytics</li>
        <li>Speech to Text capabilities</li>
      </ul>
    </div>
    <div class="abs start" style="left:276px;top:173px">START</div>

    <div class="abs plan" style="left:371px;top:79px">
      <h2>Personal</h2>
      <ul><li>Advanced customer support</li><li>Sophisticated visual avatar</li><li>Advanced analytics</li></ul>
    </div>
    <div class="abs start" style="left:470px;top:173px">START</div>

    <div class="abs plan" style="left:180px;top:203px">
      <h2>Proffesional</h2>
      <ul><li>Advanced customer support</li><li>Sophisticated visual avatar</li><li>Advanced analytics</li></ul>
    </div>
    <div class="abs start" style="left:267px;top:284px">START</div>
  </section>

  <section class="abs team">
    <div class="abs member" style="left:10px"><h3>Sarah <small>- Company Title</small></h3><div class="photo" role="img" aria-label="Team member portrait"></div>
      <ul><li>Reduce incoming calls</li><li>Reduce incoming emails</li><li>Customer support</li><li>Lorem ipsum</li><li>Dolor sit map atmu ki</li></ul></div>
    <div class="abs member" style="left:250px"><h3>Sarah <small>- Company Title</small></h3><div class="photo" role="img" aria-label="Team member portrait"></div>
      <ul><li>Reduce incoming calls</li><li>Reduce incoming emails</li><li>Customer support</li><li>Lorem ipsum</li><li>Dolor sit map atmu ki</li></ul></div>
    <div class="abs member" style="left:490px"><h3>Sarah <small>- Company Title</small></h3><div class="photo" role="img" aria-label="Team member portrait"></div>
      <ul><li>Reduce incoming calls</li><li>Reduce incoming emails</li><li>Customer support</li><li>Lorem ipsum</li><li>Dolor sit map atmu ki</li></ul></div>
    <div class="abs member" style="left:729px"><h3>Sarah <small>- Company Title</small></h3><div class="photo" role="img" aria-label="Team member portrait"></div>
      <ul><li>Reduce incoming calls</li><li>Reduce incoming emails</li><li>Customer support</li><li>Lorem ipsum</li><li>Dolor sit map atmu ki</li></ul></div>
  </section>

  <section class="abs partners">
    <span class="partner">Ostrana</span>
    <span class="partner">Brevik</span>
    <span class="partner">Calnoro</span>
    <span class="partner">Lumora <i></i></span>
    <span class="partner">Tervano</span>
    <span class="partner">Qelvix</span>
  </section>
</body>
</html>
```